Business Card Design

My company does Complete service and Maintenance for all off road toys ie: Atvs, golf carts, Dirtbikes and endures, Waverunners and Jetskis, etc... We are also taking special orders for customers and providing them with service and maintenance plans.
I want the card to appeal to young and old maybe some graphic stuff with atvs and golf carts too. We are going to offer pick up and drop off options too. Business cards and maybe brochure. Also doing Guided Waterfall Tours !
Target Market(s)
People that like to fun!
Industry/Entity Type
Business
Contact Information for Business Card
Trailblaze Garage , Daniel R Hollis ,Owner/ Technician
Danatthedunes@quillmail.net Golf Carts, Quads, Dirtbikes, and Off-Road Toys , Service and Maintenance. Ph# 507 6819 2275 Serving the Pacific Coast of Panama! Oil, Lube, and filter changes. Tuning and fine tuning, Complete details and custom orders. Order your new machine here with a complete service and Maintenance plan

```html
<!DOCTYPE html>
<html lang="en">
<head>
<meta charset="utf-8">
<title>Trailblaze Garage Business Card</title>
<link href="https://fonts.googleapis.com/css2?family=Open+Sans:wght@400;600;700&display=swap" rel="stylesheet">
<style>
  :root {
    --bg: #d9d9d9;
    --card-top: #ffffff;
    --card-bottom: #e9e9e9;
    --blue: #00aeef;
    --gray-dark: #2e2e2e;
    --gray-mid: #6a6a6a;
    --ink: #2a2a2a;
    --white: #ffffff;
  }
  * { margin: 0; padding: 0; box-sizing: border-box; }
  html, body {
    width: 1200px; height: 893px; overflow: hidden;
    background: var(--bg);
    font-family: "Open Sans", Arial, sans-serif;
  }
  .stage { position: relative; width: 1200px; height: 893px; }

  .card {
    position: absolute;
    border-radius: 30px;
    background: linear-gradient(160deg, var(--card-top) 0%, var(--card-bottom) 100%);
    box-shadow: 0 18px 40px rgba(0,0,0,0.18);
    overflow: hidden;
  }

  /* Back card: brand side */
  .card-back { left: 560px; top: 90px; width: 560px; height: 320px; }
  .brand-name {
    position: absolute; left: 46px; top: 150px;
    color: var(--blue); font-weight: 700; font-size: 30px; line-height: 1.05;
  }
  .back-gray {
    position: absolute; left: 464px; right: 0; top: 36px; height: 60px;
    background: radial-gradient(circle at 40% 40%, var(--gray-mid), var(--gray-dark) 80%);
  }
  .back-blue {
    position: absolute; left: 300px; top: 62px; width: 164px; height: 70px;
    background: var(--blue);
    display: flex; align-items: center; justify-content: center;
    color: var(--white); font-size: 8.5px; letter-spacing: 0.8px;
    white-space: nowrap;
  }

  /* Front card: contact side */
  .card-front { left: 80px; top: 460px; width: 620px; height: 354px; }
  .person {
    position: absolute; left: 0; right: 40px; top: 50px; text-align: right;
    color: var(--ink);
  }
  .person-name { font-size: 27px; font-weight: 400; letter-spacing: 0.5px; }
  .person-name strong { font-weight: 700; }
  .person-role { font-size: 12px; margin-top: -2px; letter-spacing: 0.3px; }
  .person-role strong { font-weight: 700; }

  .front-blue {
    position: absolute; left: 300px; right: 0; top: 112px; height: 102px;
    background: var(--blue);
    color: var(--white); font-size: 14px; line-height: 1.35;
    display: flex; flex-direction: column; justify-content: center;
    padding-left: 56px; white-space: nowrap;
  }
  .front-accent {
    position: absolute; left: 0; top: 196px; width: 26px; height: 96px;
    background: var(--blue);
  }
  .front-gray {
    position: absolute; left: 26px; top: 172px; width: 320px; height: 120px;
    background: linear-gradient(100deg, var(--gray-dark) 0%, var(--gray-mid) 100%);
    color: var(--white); font-size: 17px; line-height: 1.25;
    display: flex; flex-direction: column; justify-content: center;
    padding-left: 100px;
  }
  .address {
    position: absolute; left: 0; right: 0; top: 300px; text-align: center;
    padding-left: 120px;
    color: var(--ink); font-size: 12.5px; line-height: 1.3;
  }
  .address strong { font-weight: 700; }
</style>
</head>
<body>
<main class="stage">
  <section class="card card-back" aria-label="Card back">
    <div class="back-gray"></div>
    <div class="back-blue">WWW.TRAILBLAZEGARAGE.NET</div>
    <h1 class="brand-name">Trailblaze<br>Garage</h1>
  </section>

  <section class="card card-front" aria-label="Card front">
    <div class="person">
      <p class="person-name">DANIEL R <strong>HOLLIS</strong></p>
      <p class="person-role"><strong>OWNER</strong> / TECHNICIAN</p>
    </div>
    <div class="front-blue">
      <span>EMAIL &amp; WEB</span>
      <span>DANATTHEDUNES@QUILLMAIL.NET</span>
      <span>WWW.TRAILBLAZEGARAGE.NET</span>
    </div>
    <div class="front-accent"></div>
    <div class="front-gray">
      <span>PHONE &amp; FAX</span>
      <span>507 6819 2275</span>
      <span>507 6819 2276</span>
    </div>
    <p class="address">48 <strong>SHORELINE</strong> ROAD, <strong>PLAYA VERDE 0801</strong><br><strong>PANAMA</strong></p>
  </section>
</main>
</body>
</html>
```